Business card design Needed for new logo / Construction business, home extensions and new builds

We need a business card design using our new logo files which i will attach to this project :)

We are a small construction business specialising in home extensions, new builds and property development. We are very ambitious and would appreciate professional and elegant designs for our new business card.

Very serious about using the services on BriefNest and recently acquired our new logo from here :)

Please get involved, i will feedback when i can as i am very busy but can respond daily, thanks

Target Market(s)

People that want to build onto their houses, new building developments or adding too their existing property

Industry/Entity Type

Construction

Contact Information for Business Card

Hollin Marsh Construction, Tobias Renwick (Managing Director), Tel 07822200444, email - info@hollin-marsh, www.hollin-marsh.co.uk

Colors

Designer to choose colors to be used in the design.

Requirements
Must have
• I like a deep grey on the back please. A lot of you have provided black from and back, try mixing things up a little. The black looks cool 😎 Thanks

```html
<!DOCTYPE html>
<html lang="en">
<head>
<meta charset="utf-8">
<title>Hollin Marsh Construction – Business Card</title>
<link href="https://fonts.googleapis.com/css2?family=Cinzel:wght@400&family=Arimo:wght@400&display=swap" rel="stylesheet">
<style>
  :root {
    --backdrop: #1c1c1c;
    --card-grey: #333333;
    --card-edge: #3d3d3d;
    --gold: #c9a03a;
    --silver: #dcdcdc;
    --muted: #bdbdbd;
    --divider: #6a6a6a;
  }
  * { margin: 0; padding: 0; box-sizing: border-box; }
  html, body {
    width: 1200px; height: 689px; overflow: hidden;
    background: var(--backdrop);
  }
  .canvas {
    position: relative; width: 1200px; height: 689px;
    display: flex; align-items: center; justify-content: center; gap: 48px;
  }
  .card {
    position: relative; width: 530px; height: 303px;
    background: var(--card-grey);
    border: 1px solid var(--card-edge);
    border-radius: 16px;
  }
  .brand {
    display: flex; align-items: center; gap: 12px;
    font-family: "Cinzel", serif; font-weight: 400;
    color: var(--gold); text-transform: uppercase;
    line-height: 1.25;
  }
  .brand-mark {
    width: 12px; height: 12px; background: var(--gold); flex: none;
  }
  .card--front { display: flex; align-items: center; justify-content: center; }
  .card--front .brand { font-size: 24px; letter-spacing: 1px; }
  .brand-lines { display: flex; flex-direction: column; align-items: center; }
  .brand-sub { font-size: 0.7em; letter-spacing: 3px; }

  .card--back { display: flex; align-items: center; }
  .back-brand {
    width: 54%; display: flex; justify-content: center;
  }
  .back-brand .brand { font-size: 19px; }
  .divider {
    width: 1px; height: 150px;
    background: linear-gradient(var(--card-grey), var(--divider), var(--card-grey));
  }
  .contact { padding-left: 26px; font-family: "Arimo", sans-serif; }
  .person-name {
    font-family: "Cinzel", serif; font-weight: 400;
    color: var(--gold); font-size: 18px; letter-spacing: 0.5px;
  }
  .person-role { color: var(--silver); font-size: 12px; margin-top: 2px; }
  .contact-list { list-style: none; margin-top: 26px; }
  .contact-list li {
    display: flex; align-items: center; gap: 8px;
    color: var(--silver); font-size: 12.5px; line-height: 19px;
  }
  .contact-list svg { width: 11px; height: 11px; flex: none; fill: var(--gold); }
</style>
</head>
<body>
  <main class="canvas">
    <section class="card card--front" aria-label="Card front">
      <div class="brand">
        <span class="brand-mark"></span>
        <div class="brand-lines">
          <span>Hollin Marsh</span>
          <span class="brand-sub">Construction</span>
        </div>
      </div>
    </section>

    <section class="card card--back" aria-label="Card back">
      <div class="back-brand">
        <div class="brand">
          <span class="brand-mark"></span>
          <div class="brand-lines">
            <span>Hollin Marsh</span>
            <span class="brand-sub">Construction</span>
          </div>
        </div>
      </div>
      <div class="divider"></div>
      <div class="contact">
        <p class="person-name">TOBIAS RENWICK</p>
        <p class="person-role">Managing Director</p>
        <ul class="contact-list">
          <li>
            <svg viewBox="0 0 24 24" aria-hidden="true"><path d="M6.6 10.8a15.1 15.1 0 0 0 6.6 6.6l2.2-2.2c.3-.3.7-.4 1-.2 1.1.4 2.3.6 3.6.6.6 0 1 .4 1 1V20c0 .6-.4 1-1 1A17 17 0 0 1 3 4c0-.6.4-1 1-1h3.5c.6 0 1 .4 1 1 0 1.3.2 2.5.6 3.6.1.3 0 .7-.2 1z"/></svg>
            07822200444
          </li>
          <li>
            <svg viewBox="0 0 24 24" aria-hidden="true"><path d="M2 5h20v14H2z M3 6l9 7 9-7" /></svg>
            info@hollin-marsh.co.uk
          </li>
          <li>
            <svg viewBox="0 0 24 24" aria-hidden="true"><circle cx="12" cy="12" r="10"/></svg>
            www.hollin-marsh.co.uk
          </li>
        </ul>
      </div>
    </section>
  </main>
</body>
</html>
```